Supplement business needs a label design

We need a label design for our company KALVANTE LLC in The Woodlands, Texas,
This label is for a Fish Oil supplement.
Here is the task:
1. The text needs to be bold and readable on smartphone ads
2. The background is in a basic standard color like blue, silver, black, brown, etc
3. A watermark is on the background-color (waves, leaves, etc.).
4. The Brand will be "K A L V A N T E" with the attached logo design and "CU T T I N G E D G E F O R MU L A SU P P L E M E N T " :
5. Further details have to be on the label like on the attached Fish oil sample: "450 E P A / 300 D H A 1 , 2 5 0 M G DIETARY SUPPLEMENT GLUTENFREE with the icon and heart icon.
6. Please see attached samples:

```html
<!DOCTYPE html>
<html lang="en">
<head>
<meta charset="utf-8">
<title>KALVANTE Fish Oil Label</title>
<link rel="stylesheet" href="https://fonts.googleapis.com/css2?family=Montserrat:wght@500;600;700;800&display=swap">
<style>
  :root {
    --page-bg: #f3f3f3;
    --sea-deep: #1f86e6;
    --sea-mid: #3a9cf0;
    --sea-light: #5fb2f7;
    --ink-dark: #0c0f14;
    --ink-white: #ffffff;
    --accent-lime: #c9e52b;
    --accent-orange: #f0982c;
  }
  * { margin: 0; padding: 0; box-sizing: border-box; }
  html, body {
    width: 888px;
    height: 1200px;
    overflow: hidden;
    background: var(--page-bg);
    font-family: "Montserrat", sans-serif;
  }
  .canvas {
    position: relative;
    width: 888px;
    height: 1200px;
    display: flex;
    align-items: center;
    justify-content: center;
  }
  .label {
    position: relative;
    width: 888px;
    height: 470px;
    overflow: hidden;
    color: var(--ink-white);
    text-align: center;
  }
  .label__water {
    position: absolute;
    inset: 0;
    background:
      radial-gradient(ellipse 70% 30% at 30% 35%, rgba(255,255,255,0.10), transparent 70%),
      radial-gradient(ellipse 80% 25% at 75% 70%, rgba(255,255,255,0.08), transparent 70%),
      linear-gradient(170deg, var(--sea-deep) 0%, var(--sea-mid) 50%, var(--sea-light) 100%);
  }
  .brand {
    position: absolute;
    top: 88px;
    left: 0;
    right: 0;
    display: flex;
    align-items: center;
    justify-content: center;
    gap: 18px;
  }
  .brand__mark {
    width: 30px;
    height: 30px;
    border-radius: 50%;
    background: var(--ink-dark);
  }
  .brand__name {
    font-weight: 700;
    font-size: 38px;
    letter-spacing: 0.5px;
    color: var(--ink-dark);
  }
  .tagline {
    position: absolute;
    top: 188px;
    left: 0;
    right: 0;
  }
  .tagline__main {
    font-weight: 700;
    font-size: 27px;
    letter-spacing: 4.5px;
    line-height: 1;
  }
  .tagline__sub {
    margin-top: 8px;
    font-weight: 600;
    font-size: 16px;
    letter-spacing: 1.2px;
    color: var(--accent-lime);
  }
  .dosage {
    position: absolute;
    top: 284px;
    left: 0;
    right: 0;
  }
  .dosage__ratio {
    font-weight: 600;
    font-size: 17px;
    letter-spacing: 2.5px;
    color: var(--accent-orange);
  }
  .dosage__amount {
    margin-top: 16px;
    font-weight: 700;
    font-size: 13px;
    letter-spacing: 3px;
  }
  .claims {
    position: absolute;
    top: 352px;
    left: 0;
    right: 0;
    display: flex;
    align-items: center;
    justify-content: center;
    gap: 40px;
  }
  .claims__text {
    font-weight: 600;
    font-size: 11px;
    letter-spacing: 1px;
  }
  .claims__badge {
    display: flex;
    flex-direction: column;
    align-items: center;
    gap: 6px;
    font-weight: 600;
    font-size: 10px;
    letter-spacing: 1px;
  }
  .icon { display: block; }
</style>
</head>
<body>
<main class="canvas">
  <section class="label">
    <div class="label__water" role="img" aria-label="Blue underwater ripple texture background"></div>

    <div class="brand">
      <span class="brand__mark"></span>
      <span class="brand__name">KALVANTE</span>
    </div>

    <div class="tagline">
      <p class="tagline__main">CUTTING EDGE</p>
      <p class="tagline__sub">FORMULA SUPPLEMENT</p>
    </div>

    <div class="dosage">
      <p class="dosage__ratio">450 E P A / 300 D H A 1</p>
      <p class="dosage__amount">250MG</p>
    </div>

    <div class="claims">
      <svg class="icon icon--heart" width="50" height="48" viewBox="0 0 50 48" fill="none" stroke="#fff" stroke-width="3" stroke-linejoin="round" stroke-linecap="round" aria-label="Heart health">
        <path d="M25 44 C12 34 3 26 3 15 C3 8 8 3 15 3 C20 3 23 6 25 9 C27 6 30 3 35 3 C42 3 47 8 47 15 C47 26 38 34 25 44 Z"/>
        <path d="M10 24 H19 L22 18 L27 32 L31 22 H40" stroke-width="2.5"/>
      </svg>
      <span class="claims__text">DIETARY SUPPLEMENT</span>
      <div class="claims__badge">
        <svg class="icon icon--gluten-free" width="46" height="46" viewBox="0 0 46 46" fill="none" stroke="#fff" stroke-width="2.5" stroke-linecap="round" aria-label="Gluten free">
          <circle cx="23" cy="23" r="20"/>
          <line x1="23" y1="14" x2="23" y2="36"/>
          <path d="M23 20 L17 16 M23 20 L29 16 M23 26 L17 22 M23 26 L29 22 M23 32 L17 28 M23 32 L29 28"/>
          <line x1="9" y1="37" x2="37" y2="9"/>
        </svg>
        <span>GLUTEN FREE</span>
      </div>
    </div>
  </section>
</main>
</body>
</html>
```